Online eyewear company needs a couple Sign-In and Product Review page designs

We sell prescription glasses starting at $99 with Free Shipping. We have over 300 different styles and colors.Our website is under construction and we need an amazing Sign-In and Product Review Pages to help finish things off. Our brand is called VEROK and our website is called VEROKEYEWEAR.COM.

We need 5 simple sign-in and product review pages to help finish our website. Sample pages attached

We need the pages to go in order

Quick Checkout review
Sign-In
Prescription
Shipping & Payment
Final Review

Target Market(s)

20-50 that wears glasses

Industry/Entity Type

Eyewear

Colors
ffffff
919191
eaeaea
d3d3d3
dddddd
b7b7b7
000000
3176b5

Requirements
Must have
• Simple, creative, original. Must not be exactly like the photos attached. They're just templete of our casual, simple style.
• We need the pages to go in order
• Quick Checkout review
• Sign-In
• Prescription
• Shipping & Payment
• Final Review
Should not have
• Must not look exactly like the photos attached.

```html
<!DOCTYPE html>
<html lang="en">
<head>
<meta charset="utf-8">
<title>VEROK — Add a New Prescription</title>
<link rel="stylesheet" href="https://fonts.googleapis.com/css2?family=Oswald:wght@500;600&family=Poppins:ital,wght@0,300;0,400;0,500;0,600;1,400&display=swap">
<style>
  :root {
    --brand-blue: #3176b5;
    --white: #ffffff;
    --ink: #000000;
    --text: #333333;
    --muted: #919191;
    --bar-grey: #eaeaea;
    --line-grey: #d3d3d3;
    --badge: #d6007f;
  }
  * { box-sizing: border-box; margin: 0; padding: 0; }
  html, body { width: 1200px; height: 1028px; overflow: hidden; background: var(--white); }
  body { position: relative; font-family: "Poppins", sans-serif; color: var(--text); }

  .promo-bar {
    position: absolute; left: 0; top: 0; width: 1200px; height: 33px;
    background: #ececec; border-top: 1px solid var(--line-grey);
    display: flex; align-items: center; justify-content: center;
    font-size: 9px; font-weight: 500; color: var(--ink); letter-spacing: .2px;
  }

  .site-header { position: absolute; left: 0; top: 33px; width: 1200px; height: 52px; background: var(--white); }
  .brand {
    position: absolute; left: 116px; top: 9px;
    font-family: "Poppins", sans-serif; font-weight: 400; font-size: 21px;
    letter-spacing: 3px; color: var(--ink);
  }
  .main-nav { position: absolute; left: 296px; top: 18px; display: flex; gap: 18px; }
  .main-nav a { font-size: 12px; font-weight: 500; color: #444; text-decoration: none; }
  .utility-nav {
    position: absolute; left: 937px; top: 20px; display: flex; align-items: center;
    font-size: 11px; color: #555;
  }
  .utility-nav .search { display: flex; align-items: center; gap: 5px; }
  .utility-nav .divider { margin: 0 9px 0 8px; color: #777; }
  .utility-nav .sign-in { margin-left: 18px; }

  .cart-button {
    position: absolute; left: 1132px; top: 14px; width: 34px; height: 34px;
    background: var(--white); border-radius: 6px;
    box-shadow: 0 1px 4px rgba(0,0,0,.35);
    display: flex; align-items: center; justify-content: center;
  }
  .cart-count {
    position: absolute; left: 1123px; top: 5px; width: 17px; height: 17px; border-radius: 50%;
    background: var(--badge); color: var(--white); font-size: 8px;
    display: flex; align-items: center; justify-content: center;
  }

  .hero { position: absolute; left: 0; top: 85px; width: 1200px; height: 300px; background: var(--brand-blue); }
  .hero-visual {
    position: absolute; left: 150px; top: 10px; width: 860px; height: 290px;
    background: radial-gradient(ellipse at center, rgba(255,255,255,.08), rgba(255,255,255,0) 70%);
  }
  .hero-title {
    position: absolute; left: 0; top: 116px; width: 1200px; text-align: center;
    font-family: "Oswald", sans-serif; font-weight: 500; font-size: 29px; color: var(--white);
    letter-spacing: .3px;
  }
  .hero-link {
    position: absolute; left: 0; top: 160px; width: 1200px; text-align: center;
    font-style: italic; font-size: 12px; color: var(--white);
  }
  .hero-link a { color: var(--white); text-decoration: underline; text-underline-offset: 3px; }

  .checkout-steps {
    position: absolute; left: 395px; top: 417px; width: 411px; height: 36px;
    background: var(--bar-grey); border-radius: 3px; display: flex; overflow: hidden;
    font-size: 12px; color: #333;
  }
  .checkout-steps .step { display: flex; align-items: center; justify-content: center; }
  .checkout-steps .step.is-active { width: 125px; background: var(--brand-blue); color: var(--white); font-weight: 500; }
  .checkout-steps .step.shipping { width: 192px; }
  .checkout-steps .step.review { width: 94px; }

  .option-card {
    position: absolute; left: 250px; width: 701px; height: 95px; background: var(--white);
    box-shadow: 0 1px 8px rgba(0,0,0,.08);
  }
  .option-card h2 {
    position: absolute; left: 27px; top: 22px;
    font-family: "Oswald", sans-serif; font-weight: 500; font-size: 19px; color: var(--brand-blue);
  }
  .option-card p { position: absolute; left: 28px; top: 52px; font-size: 14px; color: #333; }
  .option-card .go {
    position: absolute; left: 650px; top: 30px; width: 34px; height: 34px;
    background: var(--brand-blue); border-radius: 2px;
    box-shadow: 0 3px 6px rgba(0,0,0,.25);
    display: flex; align-items: center; justify-content: center;
  }

  .order-summary {
    position: absolute; left: 250px; top: 853px; width: 702px; height: 119px;
    background: var(--brand-blue); color: var(--white); font-size: 12px;
  }
  .order-summary .row { position: absolute; left: 18px; right: 17px; display: flex; justify-content: space-between; }
  .order-summary .subtotal { top: 16px; }
  .order-summary .shipping { top: 44px; font-size: 11.5px; }
  .order-summary .shipping span:last-child { margin-right: 24px; }
  .order-summary hr { position: absolute; left: 17px; right: 17px; top: 74px; border: 0; border-top: 1px solid rgba(255,255,255,.35); }
  .order-summary .total { top: 89px; left: 16px; font-weight: 600; }
</style>
</head>
<body>
  <div class="promo-bar">FREE SHIPPING IN CONTINENTAL US</div>

  <header class="site-header">
    <div class="brand">VEROK</div>
    <nav class="main-nav">
      <a href="#">EYEGLASSES</a>
      <a href="#">ORDER LENSES</a>
    </nav>
    <div class="utility-nav">
      <span class="search">
        <svg width="12" height="12" viewBox="0 0 12 12" aria-hidden="true">
          <circle cx="5" cy="5" r="3.8" fill="none" stroke="#999" stroke-width="1.8"/>
          <line x1="7.8" y1="7.8" x2="11" y2="11" stroke="#999" stroke-width="2"/>
        </svg>
        SEARCH
      </span>
      <span class="divider">|</span>
      <span>HELP</span>
      <span class="sign-in">SIGN IN</span>
    </div>
  </header>

  <div class="cart-button" aria-label="Cart">
    <svg width="20" height="16" viewBox="0 0 20 16" aria-hidden="true">
      <path d="M6 6 L10 1 L14 6" fill="none" stroke="#000" stroke-width="1.8"/>
      <path d="M1 6 H19 L16.5 15 H3.5 Z" fill="#000"/>
      <circle cx="7" cy="10.5" r="1.1" fill="#fff"/>
      <circle cx="10" cy="10.5" r="1.1" fill="#fff"/>
      <circle cx="13" cy="10.5" r="1.1" fill="#fff"/>
    </svg>
  </div>
  <div class="cart-count">0</div>

  <section class="hero">
    <div class="hero-visual" role="img" aria-label="Faint photograph of a pair of clear eyeglass frames"></div>
    <h1 class="hero-title">ADD A NEW PRESCRIPTION</h1>
    <div class="hero-link"><a href="#">Back to prescription page</a></div>
  </section>

  <nav class="checkout-steps">
    <div class="step is-active">PRESCRIPTION</div>
    <div class="step shipping">SHIPPING &amp; PAYMENT</div>
    <div class="step review">REVIEW</div>
  </nav>

  <div class="option-card" style="top:491px">
    <h2>UPLOAD A PHOTO OF IT</h2>
    <p>this is the quickest option!</p>
    <div class="go"><svg width="12" height="14" viewBox="0 0 12 14" aria-hidden="true"><path d="M3 1.5 L9 7 L3 12.5" fill="none" stroke="#fff" stroke-width="2.2"/></svg></div>
  </div>
  <div class="option-card" style="top:605px">
    <h2>SEND IT TO US LATER</h2>
    <p>this is the quickest option!</p>
    <div class="go"><svg width="12" height="14" viewBox="0 0 12 14" aria-hidden="true"><path d="M3 1.5 L9 7 L3 12.5" fill="none" stroke="#fff" stroke-width="2.2"/></svg></div>
  </div>
  <div class="option-card" style="top:724px">
    <h2>HAVE US CALL YOUR DOCTOR</h2>
    <p>this is the quickest option!</p>
    <div class="go"><svg width="12" height="14" viewBox="0 0 12 14" aria-hidden="true"><path d="M3 1.5 L9 7 L3 12.5" fill="none" stroke="#fff" stroke-width="2.2"/></svg></div>
  </div>

  <section class="order-summary">
    <div class="row subtotal"><span>SUBTOTAL (2 ITEMS)</span><span>$240.00</span></div>
    <div class="row shipping"><span>SHIPPING</span><span>FREE</span></div>
    <hr>
    <div class="row total"><span>TOTAL</span><span>$240.00</span></div>
  </section>
</body>
</html>
```